Tallowfern Studio business cards

We are a new company based in New Zealand. We Specialize in High end Luxury Residential Architecture.

Every home is bespoke and is designed to each clients individual requirements and needs.

I like to design buildings that inspire people through light and form while offering a high level of comfort and usability.

Lines of sight, proportion and balance are fundamental to the spaces I create.
Updates

August 5th is current deadline - Today's date is the 13th of August.

Target Market(s)

New Zealanders who want a custom individual home design, typically 30-65 year old males and females

Industry/Entity Type

Architecture

Contact Information for Business Card

Director - Derek Holloway
Contact Number - 0274619037
Email - info@tallowfernstudio.co.nz
Webstie - www.tallowfernstudio.co.nz
Social Media - @tallowfernstudio

Font styles to use
Sans Serif

Requirements
Must have
• Logo (Both Sides)
Website
Email
Contact Number
Social Media

Nice to have
• Texture
Should not have
• More than 3 colours - typically I would've thought 2 would be good to match the logo.

```html
<!DOCTYPE html>
<html lang="en">
<head>
<meta charset="utf-8">
<title>Tallowfern Studio – Business Cards</title>
<link href="https://fonts.googleapis.com/css2?family=Montserrat:wght@300;400;700&display=swap" rel="stylesheet">
<style>
  :root {
    --ground: #b8962f;
    --charcoal: #333333;
    --gold: #c9a235;
    --gold-text: #c9a235;
    --ink: #111111;
  }
  * { margin: 0; padding: 0; box-sizing: border-box; }
  html, body {
    width: 1200px; height: 887px; overflow: hidden;
    background: var(--ground);
    font-family: "Montserrat", sans-serif;
  }
  .canvas { position: relative; width: 1200px; height: 887px; }

  .card {
    position: absolute;
    width: 540px; height: 308px;
    box-shadow: 0 18px 40px rgba(40, 28, 5, 0.35);
  }
  .card--front { left: 90px; top: 100px; background: var(--charcoal); color: var(--gold-text); }
  .card--back { left: 570px; top: 478px; background: var(--gold); color: var(--ink); }

  .wordmark {
    position: absolute; left: 0; right: 0;
    display: flex; align-items: center; justify-content: center; gap: 14px;
    font-weight: 400; text-transform: uppercase;
  }
  .wordmark__dot { border-radius: 50%; border: 2px solid currentColor; flex: none; }
  .card--front .wordmark { top: 56px; font-size: 15px; letter-spacing: 0.42em; }
  .card--front .wordmark__dot { width: 16px; height: 16px; }
  .card--back .wordmark { top: 136px; font-size: 22px; letter-spacing: 0.45em; }
  .card--back .wordmark__dot { width: 22px; height: 22px; }

  .person { position: absolute; left: 34px; top: 168px; }
  .person__name { font-weight: 700; font-size: 24px; letter-spacing: 0.01em; }
  .person__role { font-weight: 300; font-size: 14px; letter-spacing: 0.42em; margin-top: 2px; }

  .contact {
    position: absolute; right: 30px; top: 98px;
    text-align: right; font-weight: 300; font-size: 12.5px; line-height: 1.7;
  }
  .contact__phone { font-size: 14px; letter-spacing: 0.2em; margin-bottom: 16px; }

  .rule {
    position: absolute; left: 150px; right: 30px; top: 220px;
    height: 1px; background: var(--gold-text);
  }
  .social {
    position: absolute; left: 150px; right: 30px; top: 236px;
    display: flex; align-items: center; justify-content: center; gap: 10px;
    font-weight: 300; font-size: 13.5px;
  }
  .social__dot { width: 14px; height: 14px; border-radius: 50%; background: var(--gold-text); }
</style>
</head>
<body>
<main class="canvas">
  <section class="card card--front" aria-label="Business card front">
    <div class="wordmark"><span class="wordmark__dot"></span><span>Tallowfern Studio</span></div>
    <div class="person">
      <p class="person__name">Derek Holloway</p>
      <p class="person__role">director</p>
    </div>
    <div class="contact">
      <p class="contact__phone">027 461 9037</p>
      <p>info@tallowfernstudio.co.nz</p>
      <p>www.tallowfernstudio.co.nz</p>
    </div>
    <div class="rule"></div>
    <div class="social"><span class="social__dot"></span><span>@tallowfernstudio</span></div>
  </section>

  <section class="card card--back" aria-label="Business card back">
    <div class="wordmark"><span class="wordmark__dot"></span><span>Tallowfern Studio</span></div>
  </section>
</main>
</body>
</html>
```